Redesign of Simple Mobile App for Salesman

We want a redesign of an existing mobile app. The current app is very plain and basic. Salesman uses this app to quickly find and send information to customers while onsite.

https://apps.brelvano.com/store/apps/details?id=com.Vekarom

Target Market(s)

Internal Salesman

Industry/Entity Type

Chemical Coating

Colors

Designer to choose colors to be used in the design.

```html
<!DOCTYPE html>
<html lang="en">
<head>
<meta charset="UTF-8">
<title>Literature</title>
<link href="https://fonts.googleapis.com/css2?family=Roboto:wght@300;400;500&display=swap" rel="stylesheet">
<style>
  :root {
    --brand-blue: #3d52a6;
    --brand-blue-dark: #34479a;
    --page-bg: #ffffff;
    --status-bg: #f4f4f4;
    --ink: #1a1a1a;
    --item-active: #3b4f9f;
    --item-muted: #b4b4b4;
    --divider: #d9d9d9;
    --tab-ink: #8e8e8e;
    --tab-icon: #b9b9b9;
    --chevron: #cfcfcf;
  }
  * { box-sizing: border-box; margin: 0; padding: 0; }
  html, body { width: 811px; height: 1200px; overflow: hidden; background: var(--page-bg); }
  body { font-family: "Roboto", Arial, sans-serif; position: relative; }

  .status-bar {
    position: absolute; top: 0; left: 0; width: 811px; height: 43px;
    background: var(--status-bg); color: var(--ink);
    font-size: 22px; font-weight: 500;
  }
  .status-bar .signal { position: absolute; left: 12px; top: 11px; }
  .status-bar .clock { position: absolute; left: 0; right: 0; top: 8px; text-align: center; }
  .status-bar .battery { position: absolute; right: 12px; top: 8px; display: flex; align-items: center; gap: 6px; }

  .app-header {
    position: absolute; top: 43px; left: 0; width: 811px; height: 91px;
    background: var(--brand-blue); color: #fff;
    box-shadow: 0 6px 14px rgba(0,0,0,0.28);
    z-index: 2;
  }
  .app-header .title {
    position: absolute; left: 0; right: 0; top: 0; line-height: 91px;
    text-align: center; font-size: 33px; font-weight: 400; letter-spacing: 1.5px;
  }
  .app-header .back { position: absolute; left: 50px; top: 26px; }
  .app-header .menu { position: absolute; right: 42px; top: 24px; }

  .category-list { position: absolute; top: 180px; left: 0; width: 811px; list-style: none; }
  .category {
    position: relative; height: 130px;
    border-bottom: 2px solid var(--divider);
    display: flex; align-items: center;
    font-size: 34px; font-weight: 400; color: var(--item-muted);
  }
  .category.is-active {
    height: 128px; color: var(--item-active);
    border-top: 2px solid #ececec; border-bottom: none;
    box-shadow: 0 8px 14px rgba(0,0,0,0.22);
    z-index: 1;
  }
  .category .folder { position: absolute; left: 40px; top: 50%; transform: translateY(-50%); }
  .category .label { position: absolute; left: 122px; }
  .category .chevron { position: absolute; right: 46px; top: 50%; transform: translateY(-50%); }

  .tab-bar {
    position: absolute; left: 0; top: 1062px; width: 811px; height: 138px;
    border-top: 2px solid #e3e3e3; background: #fff;
  }
  .tab { position: absolute; top: 0; width: 160px; text-align: center; color: var(--tab-ink); font-size: 27px; }
  .tab svg { position: absolute; left: 50%; top: 26px; transform: translateX(-50%); }
  .tab .tab-label { position: absolute; left: 0; right: 0; top: 94px; }
</style>
</head>
<body>

<div class="status-bar">
  <svg class="signal" width="90" height="20" viewBox="0 0 90 20" aria-hidden="true">
    <circle cx="8" cy="10" r="6" fill="#1a1a1a"/>
    <circle cx="24" cy="10" r="6" fill="#1a1a1a"/>
    <circle cx="40" cy="10" r="6" fill="#1a1a1a"/>
    <circle cx="56" cy="10" r="6" fill="#1a1a1a"/>
    <circle cx="72" cy="10" r="5.5" fill="none" stroke="#1a1a1a" stroke-width="1.5"/>
  </svg>
  <svg style="position:absolute;left:108px;top:10px" width="28" height="22" viewBox="0 0 28 22" aria-hidden="true">
    <path d="M14 20 L2 8 A17 17 0 0 1 26 8 Z" fill="#1a1a1a"/>
  </svg>
  <div class="clock">4:21 PM</div>
  <div class="battery">100%
    <svg width="48" height="22" viewBox="0 0 48 22" aria-hidden="true">
      <rect x="1" y="2" width="40" height="18" rx="3" fill="none" stroke="#1a1a1a" stroke-width="2"/>
      <rect x="4" y="5" width="34" height="12" rx="1" fill="#1a1a1a"/>
      <rect x="43" y="7" width="3" height="8" fill="#1a1a1a"/>
    </svg>
  </div>
</div>

<header class="app-header">
  <svg class="back" width="46" height="40" viewBox="0 0 46 40" aria-label="Back">
    <path d="M44 20 H6 M20 4 L4 20 L20 36" fill="none" stroke="#fff" stroke-width="6" stroke-linecap="round" stroke-linejoin="round"/>
  </svg>
  <div class="title">LITERATURE</div>
  <svg class="menu" width="44" height="44" viewBox="0 0 44 44" aria-label="Menu">
    <circle cx="22" cy="22" r="19.5" fill="none" stroke="#fff" stroke-width="3"/>
    <path d="M12 15 H32 M12 22 H32 M12 29 H32" stroke="#fff" stroke-width="3" stroke-linecap="round"/>
  </svg>
</header>

<ul class="category-list">
  <li class="category is-active">
    <svg class="folder" width="60" height="46" viewBox="0 0 60 46" aria-hidden="true">
      <path d="M3 43 V5 H22 L27 10 H55 V43 Z M3 17 H55" fill="none" stroke="#3b4f9f" stroke-width="2.5" stroke-linejoin="round"/>
    </svg>
    <span class="label">Coating Resins</span>
    <svg class="chevron" width="40" height="40" viewBox="0 0 40 40" aria-hidden="true">
      <circle cx="20" cy="20" r="18" fill="none" stroke="#cfcfcf" stroke-width="3"/>
      <path d="M16 12 L24 20 L16 28" fill="none" stroke="#a9a9a9" stroke-width="4" stroke-linecap="round" stroke-linejoin="round"/>
    </svg>
  </li>
  <li class="category">
    <svg class="folder" width="60" height="46" viewBox="0 0 60 46" aria-hidden="true">
      <path d="M3 43 V5 H22 L27 10 H55 V43 Z M3 17 H55" fill="none" stroke="#c4c4c4" stroke-width="2.5" stroke-linejoin="round"/>
    </svg>
    <span class="label">Composite Resins</span>
    <svg class="chevron" width="40" height="40" viewBox="0 0 40 40" aria-hidden="true">
      <circle cx="20" cy="20" r="18" fill="none" stroke="#cfcfcf" stroke-width="3"/>
      <path d="M16 12 L24 20 L16 28" fill="none" stroke="#a9a9a9" stroke-width="4" stroke-linecap="round" stroke-linejoin="round"/>
    </svg>
  </li>
  <li class="category">
    <svg class="folder" width="60" height="46" viewBox="0 0 60 46" aria-hidden="true">
      <path d="M3 43 V5 H22 L27 10 H55 V43 Z M3 17 H55" fill="none" stroke="#c4c4c4" stroke-width="2.5" stroke-linejoin="round"/>
    </svg>
    <span class="label">Gel Coats</span>
    <svg class="chevron" width="40" height="40" viewBox="0 0 40 40" aria-hidden="true">
      <circle cx="20" cy="20" r="18" fill="none" stroke="#cfcfcf" stroke-width="3"/>
      <path d="M16 12 L24 20 L16 28" fill="none" stroke="#a9a9a9" stroke-width="4" stroke-linecap="round" stroke-linejoin="round"/>
    </svg>
  </li>
  <li class="category">
    <svg class="folder" width="60" height="46" viewBox="0 0 60 46" aria-hidden="true">
      <path d="M3 43 V5 H22 L27 10 H55 V43 Z M3 17 H55" fill="none" stroke="#c4c4c4" stroke-width="2.5" stroke-linejoin="round"/>
    </svg>
    <span class="label">Industrial Cleaners</span>
    <svg class="chevron" width="40" height="40" viewBox="0 0 40 40" aria-hidden="true">
      <circle cx="20" cy="20" r="18" fill="none" stroke="#cfcfcf" stroke-width="3"/>
      <path d="M16 12 L24 20 L16 28" fill="none" stroke="#a9a9a9" stroke-width="4" stroke-linecap="round" stroke-linejoin="round"/>
    </svg>
  </li>
</ul>

<nav class="tab-bar">
  <div class="tab" style="left:59px">
    <svg width="48" height="50" viewBox="0 0 48 50" aria-hidden="true">
      <path d="M24 2 L45 12 L24 22 L3 12 Z" fill="#c8c8c8"/>
      <path d="M3 15 L22 24 V48 L3 38 Z" fill="#b4b4b4"/>
      <path d="M45 15 L26 24 V48 L45 38 Z" fill="#a6a6a6"/>
    </svg>
    <span class="tab-label">Products</span>
  </div>
  <div class="tab" style="left:249px">
    <svg width="54" height="44" viewBox="0 0 54 44" aria-hidden="true">
      <rect x="1" y="4" width="52" height="38" fill="#c4c4c4"/>
      <rect x="1" y="4" width="52" height="7" fill="#a8a8a8"/>
    </svg>
    <span class="tab-label">Application</span>
  </div>
  <div class="tab" style="left:443px">
    <svg width="58" height="48" viewBox="0 0 58 48" aria-hidden="true">
      <path d="M29 8 C21 3 11 3 3 5 V42 C11 40 21 40 29 45 C37 40 47 40 55 42 V5 C47 3 37 3 29 8 Z M29 8 V45" fill="none" stroke="#b4b4b4" stroke-width="2.5" stroke-linejoin="round"/>
    </svg>
    <span class="tab-label">Literature</span>
  </div>
  <div class="tab" style="left:599px">
    <svg width="48" height="48" viewBox="0 0 48 48" aria-hidden="true">
      <circle cx="18" cy="18" r="13" fill="none" stroke="#b4b4b4" stroke-width="5"/>
      <path d="M28 28 L44 44" stroke="#b4b4b4" stroke-width="7" stroke-linecap="round"/>
    </svg>
    <span class="tab-label">Search</span>
  </div>
</nav>

</body>
</html>
```